Tavenlume: Smart Quotes for Wine Lovers

Hello. I am completing book of quotes for wine lovers. Need the text formatted so that it is easy to read and aesthetically pleasing...modern, clean, smart. Number the pages. The cover is complete. Book is small square. 7.5 by 7.5 inches. If you want to show me first few pages that would be awesome. Thank you!
Updates

I edited the quotes so if you downloaded first ones, please grab these ones instead, thank you! 

Target Market(s)

wine lovers. Urban. Modern.

Industry/Entity Type

Quotes

Requirements
Should not have
• No color. black and white only.

```html
<!DOCTYPE html>
<html lang="en">
<head>
<meta charset="UTF-8">
<title>Tavenlume – Smart Quotes for Wine Lovers, pages 36–37</title>
<link rel="stylesheet" href="https://fonts.googleapis.com/css2?family=Noto+Sans:wght@400;700&display=swap">
<style>
  :root {
    --paper: #ffffff;
    --ink: #111111;
    --note: #8a8a8a;
    --gutter: #c8c8c8;
  }
  html, body {
    margin: 0;
    padding: 0;
    width: 1200px;
    height: 600px;
    overflow: hidden;
    background: var(--paper);
  }
  .spread {
    position: relative;
    width: 1200px;
    height: 600px;
    display: flex;
    font-family: "Noto Sans", Verdana, sans-serif;
    color: var(--ink);
  }
  .page {
    position: relative;
    width: 600px;
    height: 600px;
  }
  .page--left { border-right: 1px solid var(--gutter); box-sizing: border-box; }
  .quote {
    position: absolute;
    top: 206px;
    left: 0;
    right: 0;
    margin: 0;
    text-align: center;
    font-size: 33px;
    line-height: 40px;
    font-weight: 400;
    letter-spacing: 0.6px;
  }
  .page--left .quote { left: -12px; }
  .attribution {
    position: absolute;
    top: 424px;
    left: 0;
    right: 0;
    margin: 0;
    text-align: center;
    font-size: 13px;
    letter-spacing: 1px;
    text-transform: uppercase;
  }
  .page--left .attribution { left: -12px; }
  .author-note {
    position: absolute;
    top: 518px;
    left: 0;
    right: 0;
    margin: 0;
    text-align: center;
    font-size: 7.5px;
    line-height: 10px;
    font-weight: 700;
    color: var(--note);
  }
  .page-number {
    position: absolute;
    top: 522px;
    font-size: 13px;
    margin: 0;
  }
  .page--left .page-number { left: 78px; }
  .page--right .page-number { right: 80px; }
</style>
</head>
<body>
  <main class="spread">
    <section class="page page--left">
      <p class="quote">The connoisseur does<br>not drink wine<br>&nbsp;but tastes its secrets</p>
      <p class="attribution">–Mateo Varensol</p>
      <p class="author-note">Mateo Andrés Varensol i Cortada,<br>Painter of dreamlike coastal scenes (1911–1978) Catalan Modern Artist.</p>
      <p class="page-number">36</p>
    </section>
    <section class="page page--right">
      <p class="quote">Wine is the divine juice<br>of September.</p>
      <p class="attribution">–Lucien Morvaux</p>
      <p class="author-note">Lucien-Henri Daveraux, best remembered by his pen name Morvaux.<br>(1722 –1801). Parisian Essayist, Critic and Storyteller of the Salons.</p>
      <p class="page-number">37</p>
    </section>
  </main>
</body>
</html>
```